Building Servicess

We need a new business card design for a company. We specialise in: Electrical/Site temporary electrics, Data/Network Installation, Passive Fire Protection

Industry/Entity Type

Construction

Contact Information for Business Card

Services provided as detailed on project description

Font styles to use
Serif

Colors
0054AA
0677BA
7BADD7
CADEEF
E8F1F8
00AB8E
00BBA5
67D7C9
C6EFE9
E9F9F6
EB3D1F
EC4F4E
F09395
F8D3D4
FCEDEE

Requirements
Must have
• Company logo-contact details-phone numbers

```html
<!DOCTYPE html>
<html lang="en">
<head>
<meta charset="utf-8">
<title>Brantwell Site Services – Business Card</title>
<link rel="stylesheet" href="https://fonts.googleapis.com/css2?family=Montserrat:wght@400;500;700&display=swap">
<style>
  :root {
    --bg: #e2e4e4;
    --blue-deep: #1f55a6;
    --blue-main: #2b62b0;
    --blue-light: #3a78c0;
    --card-white: #f4f5f6;
    --card-grey: #e6e8ea;
    --ink-grey: #6d7278;
    --rule-grey: #a9adb1;
    --white: #ffffff;
  }
  * { box-sizing: border-box; margin: 0; padding: 0; }
  html, body { width: 1200px; height: 1000px; overflow: hidden; }
  body {
    background: var(--bg);
    font-family: "Montserrat", sans-serif;
    position: relative;
  }
  .card {
    position: absolute;
    width: 525px;
    height: 300px;
    border-radius: 26px;
    overflow: hidden;
    box-shadow: 0 14px 28px rgba(0,0,0,0.18);
  }
  /* Front */
  .card--front {
    left: 130px;
    top: 140px;
    background: linear-gradient(135deg, var(--blue-deep) 0%, var(--blue-main) 50%, var(--blue-light) 100%);
  }
  .front-bands { position: absolute; inset: 0; }
  .front-name {
    position: absolute;
    left: 0; right: 0; top: 112px;
    text-align: center;
    color: var(--white);
    font-weight: 700;
    font-size: 30px;
    letter-spacing: 1px;
    line-height: 1.15;
  }
  /* Back */
  .card--back {
    left: 545px;
    top: 540px;
    background: linear-gradient(160deg, var(--card-white) 0%, var(--card-grey) 100%);
  }
  .back-band {
    position: absolute;
    left: 0; right: 0; bottom: 0;
    height: 46px;
    background: linear-gradient(90deg, var(--blue-deep), var(--blue-light));
  }
  .back-brand {
    position: absolute;
    left: 30px; top: 96px;
    width: 200px;
    color: var(--blue-main);
    font-weight: 700;
    font-size: 20px;
    line-height: 1.2;
    text-align: center;
  }
  .back-divider {
    position: absolute;
    left: 260px; top: 42px;
    width: 1px; height: 170px;
    background: var(--rule-grey);
  }
  .contact {
    position: absolute;
    left: 282px; top: 44px;
    color: var(--ink-grey);
  }
  .contact__name {
    color: var(--blue-main);
    font-weight: 700;
    font-size: 19px;
    letter-spacing: 0.5px;
  }
  .contact__title {
    font-size: 10px;
    letter-spacing: 1px;
    margin-bottom: 14px;
  }
  .contact__list { list-style: none; }
  .contact__item {
    display: flex;
    align-items: flex-start;
    gap: 8px;
    font-size: 13px;
    line-height: 1.35;
    margin-bottom: 4px;
  }
  .contact__icon { width: 12px; height: 12px; margin-top: 3px; flex: none; fill: var(--blue-main); }
</style>
</head>
<body>

<section class="card card--front" aria-label="Business card front">
  <svg class="front-bands" viewBox="0 0 525 300" aria-hidden="true">
    <polygon points="40,300 120,0 170,0 90,300" fill="#ffffff" opacity="0.05"/>
    <polygon points="110,300 190,0 230,0 150,300" fill="#000000" opacity="0.05"/>
    <polygon points="0,240 525,110 525,150 0,280" fill="#ffffff" opacity="0.04"/>
  </svg>
  <div class="front-name">BRANTWELL<br>SITE SERVICES</div>
</section>

<section class="card card--back" aria-label="Business card back">
  <div class="back-band"></div>
  <div class="back-brand">BRANTWELL<br>SITE SERVICES</div>
  <div class="back-divider"></div>
  <div class="contact">
    <h1 class="contact__name">MAREK OLSZEWSKI</h1>
    <p class="contact__title">MANAGING DIRECTOR</p>
    <ul class="contact__list">
      <li class="contact__item">
        <svg class="contact__icon" viewBox="0 0 24 24"><path d="M6.6 10.8a15.1 15.1 0 0 0 6.6 6.6l2.2-2.2c.3-.3.7-.4 1-.2 1.1.4 2.3.6 3.6.6.6 0 1 .4 1 1V20c0 .6-.4 1-1 1A17 17 0 0 1 3 4c0-.6.4-1 1-1h3.5c.6 0 1 .4 1 1 0 1.3.2 2.5.6 3.6.1.3 0 .7-.2 1z"/></svg>
        <span>020 3946 0718</span>
      </li>
      <li class="contact__item">
        <svg class="contact__icon" viewBox="0 0 24 24"><path d="M7 1h10a2 2 0 0 1 2 2v18a2 2 0 0 1-2 2H7a2 2 0 0 1-2-2V3a2 2 0 0 1 2-2zm0 3v15h10V4z"/></svg>
        <span>07700900482</span>
      </li>
      <li class="contact__item">
        <svg class="contact__icon" viewBox="0 0 24 24"><path d="M12 2a10 10 0 1 0 0 20 10 10 0 0 0 0-20zm6.9 6h-2.9a15.6 15.6 0 0 0-1.4-3.6A8 8 0 0 1 18.9 8zM12 4c.8 1.2 1.5 2.5 1.9 4h-3.8c.4-1.4 1.1-2.8 1.9-4zM4.3 14a8 8 0 0 1 0-4h3.4a16 16 0 0 0 0 4zm.8 2h2.9c.3 1.3.8 2.5 1.4 3.6A8 8 0 0 1 5.1 16zM8 8H5.1a8 8 0 0 1 4.3-3.6C8.8 5.5 8.4 6.7 8 8zm4 12c-.8-1.2-1.5-2.5-1.9-4h3.8c-.4 1.4-1.1 2.8-1.9 4zm2.3-6H9.7a14.7 14.7 0 0 1 0-4h4.6a14.7 14.7 0 0 1 0 4zm.3 5.6c.6-1.1 1.1-2.3 1.4-3.6h2.9a8 8 0 0 1-4.3 3.6zm1.7-5.6a16 16 0 0 0 0-4h3.4a8 8 0 0 1 0 4z"/></svg>
        <span>brantwellsite.co.uk</span>
      </li>
      <li class="contact__item">
        <svg class="contact__icon" viewBox="0 0 24 24"><path d="M12 2a7 7 0 0 0-7 7c0 5.2 7 13 7 13s7-7.8 7-13a7 7 0 0 0-7-7zm0 9.5a2.5 2.5 0 1 1 0-5 2.5 2.5 0 0 1 0 5z"/></svg>
        <span>Harrow Lane,<br>Brentwood, Essex,<br>CM14 9QT</span>
      </li>
    </ul>
  </div>
</section>

</body>
</html>
```